Dovamel Nutrition Supplement Jar

Label for jar. White label on a brown bottle jar.
Conservative look, should look like medicine.
Main Side:
Oak Harbor Clinics (smaller size) (with logo)
DOVAMEL 10mg (large size)
Doctor Formulated
Developed in Clinical Practice
60 Capsules
(I prefer the single color white label with dark brown letters. Please stay close to that design)
(For the back side, please use the multicolor set up)
(The whole Label should be one color - white with dark brown letters)
Please visit my site for more inspiration and feel: www.velmorine.example
The product will be brown jar listed on this site.
Can you please provide one version without the text "Oak Harbor Clinics & Logo".
Thank you.

Target Market(s)

Women, 34-59 years old

Industry/Entity Type

Nutrition

Requirements
Should not have
• Multicolors, leaves,

```html
<!DOCTYPE html>
<html lang="en">
<head>
<meta charset="utf-8">
<title>Dovamel Label</title>
<link href="https://fonts.googleapis.com/css2?family=Rubik:wght@300;400;500;700;900&family=Lato:wght@900&family=Raleway:wght@500;700&display=swap" rel="stylesheet">
<style>
:root{
  --page:#f7f3f2;
  --label:#fbfafa;
  --brown:#521712;
  --brown-soft:#6b3a34;
  --ink:#2f2624;
  --muted:#4a3b39;
}
*{margin:0;padding:0;box-sizing:border-box}
html,body{width:1200px;height:1200px;overflow:hidden;background:var(--page)}
.label{position:absolute;left:29px;top:414px;width:1142px;height:373px;background:var(--label);box-shadow:0 6px 24px rgba(0,0,0,.12);font-family:"Rubik",sans-serif;font-weight:300;color:var(--ink)}
.block{position:absolute}
.directions,.warning{left:33px;width:289px;font-size:11.4px;line-height:14.4px;text-align:justify}
.directions{top:44px}
.warning{top:146px;left:35px}
.directions b,.warning b{font-weight:500;color:var(--ink)}
.fda-box{left:39px;top:282px;width:279px;height:48px;border:2px solid var(--brown);padding:3px 6px;font-size:10.4px;line-height:13.4px;font-weight:500}
.brand-mark{left:551px;top:58px;width:40px;height:40px;border-radius:50%;background:var(--brown)}
.brand{left:350px;width:440px;text-align:center}
.brand-name{top:152px;font-family:"Lato",sans-serif;font-weight:900;font-size:47px;letter-spacing:2px;color:var(--brown);line-height:56px}
.brand-rule{position:absolute;left:462px;top:210px;width:218px;height:4px;background:var(--brown)}
.brand-dose{top:222px;font-family:"Rubik",sans-serif;font-weight:400;font-size:25px;color:var(--brown)}
.claims{left:453px;top:272px;width:232px;color:var(--brown-soft)}
.claims h4{font-family:"Raleway",sans-serif;font-weight:700;font-size:8px;color:var(--brown)}
.claims p{font-size:6.5px;line-height:8.7px;text-align:justify;text-transform:uppercase;color:var(--muted);margin-top:2px}
.claims .dev{margin-top:3px}
.claims .count{margin-top:12px;font-size:9.8px}
.facts{left:868px;top:9px;width:260px;height:193px;border:2px solid var(--brown);padding:9px 8px 0 8px;color:var(--muted)}
.facts h3{font-weight:700;font-size:21px;color:var(--brown);line-height:24px}
.facts .row{display:flex;justify-content:space-between;font-size:9.4px;line-height:10.6px}
.facts .row:first-of-type{margin-top:10px}
.facts .bar{height:6px;background:var(--brown);margin-top:12px}
.facts .blend{font-size:8.2px;margin-top:7px;padding-bottom:6px;border-bottom:1.5px solid var(--brown);white-space:nowrap}
.facts .ingredients{font-size:9.4px;line-height:11.8px;text-align:justify;margin-top:7px;padding:0 1px}
.maker{left:869px;top:229px;width:270px;color:var(--muted);font-size:11px;line-height:13.6px}
.maker .company{font-weight:700;font-size:17px;color:var(--brown);line-height:22px;margin-top:4px}
.maker .address{margin-top:13px}
.base-band{position:absolute;left:0;bottom:0;width:100%;height:11px;background:var(--brown)}
</style>
</head>
<body>
<main class="label">
  <p class="block directions"><b>Directions:</b> Take one or two capsules after meals. Do not exceed three capsules per day. Take during real&#8209;time cravings or before drinking situations for additional craving support. Store in a cool dry place, tightly closed. Keep away from children.</p>
  <p class="block warning"><b>Warning:</b> Not to be used by children under 18 years, women who are pregnant, may become pregnant, breastfeeding, people taking antidepressant drugs or sedatives. If you are under a physician’s care or taking any medications, or being treated for heart disease or diabetes, consult your health care professional before taking this product.</p>
  <p class="block fda-box">The FDA has not evaluated these statements. This product is not intended to diagnose, treat, cure, or prevent any disease.</p>

  <div class="block brand-mark"></div>
  <h1 class="block brand brand-name">DOVAMEL</h1>
  <div class="brand-rule"></div>
  <p class="block brand brand-dose">10MG</p>
  <div class="block claims">
    <h4>DOCTOR FORMULATED</h4>
    <p>In synergy our ingredients act on neuro-receptors and reward system pathways in the brain. Reduce cravings and mechanisms of addiction, promote motivation and positive behavior.</p>
    <h4 class="dev">DEVELOPED IN CLINICAL PRACTICE</h4>
    <h4 class="count">60 CAPSULES</h4>
  </div>

  <section class="block facts">
    <h3>Supplement Facts</h3>
    <div class="row"><span>Serving Size:</span><span>1 capsule</span></div>
    <div class="row"><span>Servings per Container:</span><span>60</span></div>
    <div class="bar"></div>
    <p class="blend">Proprietary Formula: 1800 mg (% of Daily Value not Established)</p>
    <p class="ingredients">Thiamin hydrochloride, Riboflavin, Niacinamide, Pyridoxine hydrochloride, Folic Acid, Cyanocobalamin, Biotin, Pueraria Root, Lithium Orotate, Gentian Root, Bupleurum Root, Milk Thistle Seed Extract, Angelica Root, Chanca Piedra, Dandelion Root, Rhodiola Rosea, Saffron.</p>
  </section>

  <div class="block maker">
    <p>Manufactured in the USA for</p>
    <p class="company">Harborline Wellness LLC</p>
    <p>from Globally Sourced Ingredients</p>
    <p class="address">Harborline Wellness LLC,<br>Fairhaven, Colorado<br>Ph. 555-010-4471,<br>www.velmorine.example</p>
  </div>

  <div class="base-band"></div>
</main>
</body>
</html>
```